Multilingual Website for a Curaline Company

We need a multilingual Website for our Curaline company that sells gloves and masks, the website should have 3-5 subpages on 5 different languages.

Industry/Entity Type

Medtech

Number of Pages Required

5+ page

Requirements
Must have
• Unique Design - No template
Should not have
• No Templates

```html
<!DOCTYPE html>
<html lang="en">
<head>
<meta charset="utf-8">
<title>Curaline – Cart</title>
<link href="https://fonts.googleapis.com/css2?family=Lato:wght@400;700&display=swap" rel="stylesheet">
<style>
:root{
  --forest:#172611;
  --forest-band:#1e3215;
  --leaf:#4b6b2b;
  --brand:#5ea52b;
  --ink:#2b2b2b;
  --muted:#555;
  --rule:#ebebeb;
  --white:#fff;
}
*{box-sizing:border-box;margin:0;padding:0}
html,body{width:1200px;height:746px;overflow:hidden;background:var(--white);font-family:'Lato',sans-serif;color:var(--ink)}
.page{position:relative;width:1200px;height:746px}
.abs{position:absolute}
.site-header{position:absolute;left:0;top:0;width:1200px;height:67px;background:var(--forest)}
.brand{position:absolute;font-weight:700;font-size:30px;color:var(--brand);display:flex;align-items:center;gap:8px;letter-spacing:.5px}
.brand .mark{width:16px;height:16px;background:var(--brand)}
.main-nav a{position:absolute;top:21px;color:var(--white);font-weight:700;font-size:17px;text-decoration:none}
.header-icons svg{position:absolute}
.cart-badge{position:absolute;left:1034px;top:18px;width:15px;height:15px;border-radius:50%;background:var(--leaf);color:var(--white);font-size:9px;font-weight:700;display:flex;align-items:center;justify-content:center}
.col-head{position:absolute;top:123px;font-size:13.5px;color:var(--ink);letter-spacing:.2px}
.rule{position:absolute;background:var(--rule)}
.cell{position:absolute;font-size:12px;color:var(--muted)}
.product-name{position:absolute;left:248px;top:172px;font-size:14px;color:var(--ink)}
.product-thumb{position:absolute;left:183px;top:162px;width:40px;height:38px;border-radius:6px;background:linear-gradient(135deg,#dfe8ee,#3a3a3a)}
.qty{position:absolute;left:508px;top:164px;width:42px;height:35px;border:1px solid #ccc;font-size:12px;display:flex;align-items:center;justify-content:center}
.btn{position:absolute;display:flex;align-items:center;justify-content:center;font-size:12.5px;font-weight:700;color:var(--white)}
.btn-dark{background:var(--forest)}
.btn-green{background:var(--leaf)}
.coupon{position:absolute;left:150px;top:233px;width:114px;height:38px;border:1px solid #ccc;font-size:12.5px;display:flex;align-items:center;justify-content:center;color:var(--ink)}
.totals{position:absolute;left:750px;top:126px;width:300px;height:300px;background:var(--white);box-shadow:0 1px 8px rgba(0,0,0,.16)}
.totals h2{position:absolute;right:15px;top:26px;font-size:14px;font-weight:400}
.totals .label{position:absolute;left:15px;font-size:12px;font-weight:700;color:#333}
.totals .value{position:absolute;right:15px;font-size:12px;color:#444}
.totals .line{position:absolute;left:15px;width:270px;height:3px;background:var(--rule)}
.site-footer{position:absolute;left:0;top:488px;width:1200px;height:223px;background:var(--forest);color:var(--white)}
.footer-about{position:absolute;left:154px;top:68px;width:260px;font-size:14px;line-height:20.3px}
.footer-head{position:absolute;top:35px;font-size:17.5px;font-weight:700}
.footer-link{position:absolute;font-size:14px}
.contact-text{position:absolute;left:919px;font-size:14px;line-height:20px}
.copyright{position:absolute;left:0;top:711px;width:1200px;height:35px;background:var(--forest-band);color:var(--white);font-size:14px;display:flex;align-items:center;justify-content:center}
</style>
</head>
<body>
<div class="page">
  <header class="site-header">
    <div class="brand" style="left:150px;top:13px"><span class="mark"></span>curaline</div>
    <nav class="main-nav">
      <a style="left:458px">Home</a>
      <a style="left:534px">Shop</a>
      <a style="left:603px">About</a>
      <a style="left:681px">Contact</a>
    </nav>
    <div class="header-icons">
      <svg style="left:877px;top:32px" width="25" height="16" viewBox="0 0 25 16">
        <rect width="25" height="16" fill="#1f3f8f"/>
        <path d="M0 0L25 16M25 0L0 16" stroke="#fff" stroke-width="3.5"/>
        <path d="M0 0L25 16M25 0L0 16" stroke="#c8102e" stroke-width="1.2"/>
        <path d="M12.5 0V16M0 8H25" stroke="#fff" stroke-width="5"/>
        <path d="M12.5 0V16M0 8H25" stroke="#c8102e" stroke-width="3"/>
      </svg>
      <svg style="left:922px;top:25px" width="26" height="26" viewBox="0 0 26 26" fill="none" stroke="#fff" stroke-width="1.8">
        <circle cx="10.5" cy="10.5" r="9"/><path d="M17 17l8 8"/>
      </svg>
      <svg style="left:971px;top:24px" width="26" height="28" viewBox="0 0 26 28" fill="none" stroke="#fff" stroke-width="1.8">
        <circle cx="13" cy="8" r="7"/><path d="M1 27c0-7 5-11 12-11s12 4 12 11"/>
      </svg>
      <svg style="left:1014px;top:27px" width="26" height="25" viewBox="0 0 26 25" fill="none" stroke="#fff" stroke-width="1.8">
        <path d="M1 2h4l3 14h14l3-10H7"/><circle cx="10" cy="21" r="2"/><circle cx="20" cy="21" r="2"/>
      </svg>
    </div>
    <div class="cart-badge">1</div>
  </header>

  <section class="cart-table">
    <div class="col-head" style="left:248px">PRODUCT</div>
    <div class="col-head" style="left:417px">PRICE</div>
    <div class="col-head" style="left:507px">QUANTITY</div>
    <div class="col-head" style="left:627px">SUBTOTAL</div>
    <div class="rule" style="left:150px;top:144px;width:562px;height:3px"></div>
    <svg class="abs" style="left:151px;top:174px" width="14" height="14" viewBox="0 0 14 14" stroke="#222" stroke-width="2"><path d="M1 1l12 12M13 1L1 13"/></svg>
    <div class="product-thumb" role="img" aria-label="Product photo of a reusable face mask"></div>
    <div class="product-name">Reusable Mask</div>
    <div class="cell" style="left:417px;top:174px">$26.00</div>
    <div class="qty">1</div>
    <div class="cell" style="left:629px;top:174px">$26.00</div>
    <div class="rule" style="left:150px;top:214px;width:562px;height:3px"></div>
    <div class="coupon">Coupon code</div>
    <div class="btn btn-dark" style="left:272px;top:233px;width:150px;height:38px">Apply coupon</div>
    <div class="btn btn-green" style="left:562px;top:233px;width:150px;height:38px">Update cart</div>
  </section>

  <aside class="totals">
    <h2>Cart total</h2>
    <div class="label" style="top:60px">Subtotal</div><div class="value" style="top:60px">$26.00</div>
    <div class="line" style="top:86px"></div>
    <div class="label" style="top:104px">Shipping</div><div class="value" style="top:104px">Free shipping</div>
    <div class="line" style="top:131px"></div>
    <div class="label" style="top:149px">Tax</div><div class="value" style="top:149px">$0.00</div>
    <div class="line" style="top:175px"></div>
    <div class="label" style="top:193px">Total</div><div class="value" style="top:193px">$26.00</div>
    <div class="btn btn-green" style="left:76px;top:234px;width:150px;height:38px">Proceed to checkout</div>
  </aside>

  <footer class="site-footer">
    <div class="brand" style="left:150px;top:14px"><span class="mark"></span>curaline</div>
    <p class="footer-about">Lorem ipsum dolor sit amet, consectetur adipiscing elit. Morbi pellentesque, nisi ac tincidunt varius, erat nulla tempor est, ac malesuada ex quam sit amet ipsum.</p>
    <div class="footer-head" style="left:555px">Navigation</div>
    <div class="footer-link" style="left:555px;top:67px">Home</div>
    <div class="footer-link" style="left:555px;top:94px">Shop</div>
    <div class="footer-link" style="left:555px;top:121px">About</div>
    <div class="footer-link" style="left:555px;top:148px">Contact</div>
    <div class="footer-link" style="left:640px;top:67px">Privacy Policy</div>
    <div class="footer-link" style="left:640px;top:94px">Returns &amp; Refunds</div>
    <div class="footer-link" style="left:640px;top:121px">FAQs</div>
    <div class="footer-head" style="left:885px">Contact Us</div>
    <svg class="abs" style="left:886px;top:66px" width="15" height="22" viewBox="0 0 15 22" fill="none" stroke="#fff" stroke-width="1.4"><path d="M7.5 21S1 12.5 1 7.5a6.5 6.5 0 0113 0C14 12.5 7.5 21 7.5 21z"/><circle cx="7.5" cy="7.5" r="2.5"/></svg>
    <div class="contact-text" style="top:65px">Address, City, Country<br>Exact address</div>
    <svg class="abs" style="left:885px;top:127px" width="20" height="20" viewBox="0 0 20 20" fill="#fff"><path d="M4 1l3 4-2 2c1 3 4 6 7 7l2-2 4 3-2 3C9 18 2 11 1 3z"/><path d="M12 1a7 7 0 017 7M12 4a4 4 0 014 4" fill="none" stroke="#fff" stroke-width="1.3"/></svg>
    <div class="contact-text" style="top:127px">+00 0 0000 00000</div>
    <svg class="abs" style="left:885px;top:171px" width="20" height="14" viewBox="0 0 20 14" fill="none" stroke="#fff" stroke-width="1.4"><rect x=".7" y=".7" width="18.6" height="12.6"/><path d="M.7 .7L10 8l9.3-7.3M.7 13.3l7-6M19.3 13.3l-7-6"/></svg>
    <div class="contact-text" style="top:168px">admin@curaline.com</div>
  </footer>
  <div class="copyright">Curaline 2020 All Rights Reserved.</div>
</div>
</body>
</html>
```